Flyer-Design für Medizinische Fusspflege
Zielgruppe
Medizinische fusspflege, meistens mittelalterliche und ältere Menschen , Problematik auf Füßen, Diabätiker und etc.
Spezialisiert in medizinischen Bereich
Ich bin angehende Polologin (medizinische Fusspflegerin) und mache mich ab 01.05 20120 mit einer pysiopraxis selbstständig.
Ich bin Angehende Polologin (medizinische Fusspflegerin) und mache mich ab 01. 05.20120in einer Pysiotherapie Praxis Brandauer selbstständig.
Die Zielgruppe für diesen Flyer (zweiseitig) sollen Alters- und Seniorenheime sein, bei denen ich die Behandlung vor Ort durchführe. Somit sollte auch Mobilität mit einbezogen werden.
Aufgabenstellung
Es ist mir wichtig das der Flyer (zweiseitig) möglichst klar strukturiert ist um das Interesse zu wecken.
Vom Format her sind wir relativ frei, egal ob Postkartengröße, oder DIN lang, oder DIN A5 ist eigentlich alles möglich, je nach Design aber zweiseitig sollte er sein.
Mein neues Logo ( sanft im Gang soll dabei genauso zur Geltung kommen wie meine eigentlich Tätigkeit.
Hervorgehoben werden soll das ich ab dem 01.05.2010 verfügbar bin, durch einen Button auf der Vorderseite.
Folgender Text sollte auf die Rückseite:
Mein Leistungsportfolio:
- Medizinische Fußpflege
- Therapie Diabetischem Fuß
- Hilfe bei eingewachsenen Nägeln
- Spangentherapie
- Druckschutz / Orthose
- Hilfe bei Hühneraugen, Schrunden
- Unterstützung bei Nagel- und Fußpilzbehandlung
- Fußmassage
- Nagelprothetik
Branche
Ärzte/Gesundheit
Liefern Sie eigene Bilder oder sollen die Designer Bildmaterial aus kommerziellen Bilddatenbanken (Stockmaterial) verwenden?
Ich bin noch unentschieden.
Welche Wirkung soll Ihr Design erzielen?
KlassischModern
ErschwinglichLuxuriös
SchnörkellosVerspielt
Preisliste sol auch dazu
Medizinische Fußpflege 42,50€
Nagelkorrektur Ungilan 40€
Teilbehandlung 27,50
Nage..
Meine Web Seite www.fusspflege-horbenau.de

```html
<!DOCTYPE html>
<html lang="de">
<head>
<meta charset="utf-8">
<title>Sanft im Gang – Flyer</title>
<link href="https://fonts.googleapis.com/css2?family=Montserrat:wght@400;500;600&display=swap" rel="stylesheet">
<style>
  :root{
    --green:#7a9a1e;
    --teal:#1e6f85;
    --ink:#555;
    --band:#f8eeee;
    --paper:#fff;
  }
  html,body{margin:0;padding:0;overflow:hidden;background:var(--paper);}
  .canvas{position:relative;width:1200px;height:1200px;overflow:hidden;font-family:'Montserrat',sans-serif;}
  .card{position:absolute;width:730px;height:515px;overflow:hidden;background:var(--paper);box-shadow:0 8px 18px rgba(0,0,0,.25);}
  .card--front{left:69px;top:54px;}
  .card--back{left:386px;top:623px;background:linear-gradient(160deg,#fff 30%,#fbf3f2 70%,#fff 100%);}
  .card svg.shapes{position:absolute;inset:0;}
  .brand{position:absolute;margin:0;color:var(--green);font-weight:400;white-space:nowrap;}
  .card--front .brand{left:59px;top:62px;font-size:31px;}
  .card--back .brand{left:358px;top:34px;font-size:19px;transform:translateX(-50%);}
  .availability{position:absolute;left:588px;top:300px;width:112px;height:112px;border-radius:50%;background:var(--green);color:#fff;display:flex;flex-direction:column;align-items:center;justify-content:center;text-align:center;margin:0;font-size:12px;line-height:15px;font-weight:500;}
  .availability strong{font-size:20px;line-height:24px;font-weight:600;}
  .front-title{position:absolute;left:0;width:100%;top:444px;margin:0;text-align:center;font-size:24px;font-weight:600;color:var(--ink);}
  .front-url{position:absolute;left:0;width:100%;top:479px;margin:0;text-align:center;font-size:14px;color:var(--ink);}
  .services{position:absolute;left:208px;top:68px;width:300px;margin:0;text-align:center;font-size:10.5px;line-height:14px;color:var(--ink);}
  .services strong{color:var(--green);font-weight:600;}
  .about{position:absolute;right:400px;top:158px;width:320px;text-align:right;color:var(--teal);}
  .about h2{margin:0 0 8px;font-size:25px;font-weight:600;}
  .about p{margin:0;font-size:14.3px;line-height:20.9px;}
  .prices{position:absolute;left:391px;top:220px;width:322px;color:var(--green);}
  .prices h2{margin:0 0 8px;font-size:23px;font-weight:600;}
  .price-list{list-style:none;margin:0;padding:0;font-size:14.3px;line-height:20.9px;}
  .price-list li{display:flex;align-items:baseline;white-space:nowrap;}
  .price-list .dots{flex:1;border-bottom:1px dotted var(--green);margin:0 1px 4px;}
  .price-list small{font-size:11.5px;}
  .address,.contact{position:absolute;top:440px;margin:0;font-size:13.8px;line-height:18px;color:var(--ink);font-style:normal;}
  .address{right:400px;text-align:right;}
  .contact{left:391px;}
</style>
</head>
<body>
<div class="canvas">

  <!-- Vorderseite -->
  <section class="card card--front">
    <svg class="shapes" width="730" height="515" viewBox="0 0 730 515">
      <defs>
        <linearGradient id="heroTone" x1="0" y1="0" x2="1" y2="1">
          <stop offset="0" stop-color="#f4ece8"/>
          <stop offset=".35" stop-color="#eebfae"/>
          <stop offset=".6" stop-color="#f1d3c7"/>
          <stop offset=".85" stop-color="#f7c58a"/>
          <stop offset="1" stop-color="#f6efea"/>
        </linearGradient>
      </defs>
      <rect width="730" height="470" fill="url(#heroTone)" role="img" aria-label="Foto: Hände bei einer sanften Fußmassage, Handtuch und orange Blüte im Hintergrund"/>
      <path d="M0 458 Q365 400 730 461 L730 515 L0 515 Z" fill="var(--band)"/>
      <path d="M0 458 Q365 400 730 461" fill="none" stroke="var(--green)" stroke-width="2.5"/>
    </svg>
    <p class="brand">Sanft im Gang</p>
    <p class="availability">Für Sie da ab<strong>01.05.</strong>auch mobil</p>
    <h1 class="front-title">Medizinische Fußpflege vor Ort</h1>
    <p class="front-url">www.fusspflege-horbenau.de</p>
  </section>

  <!-- Rückseite -->
  <section class="card card--back">
    <svg class="shapes" width="730" height="515" viewBox="0 0 730 515">
      <path d="M0 0 L191 0 A175 175 0 0 1 0 161 Z" fill="#e9dedc" role="img" aria-label="Porträtfoto der Fußpflegerin"/>
      <path d="M191 0 A175 175 0 0 1 0 161" fill="none" stroke="var(--teal)" stroke-width="3"/>
      <path d="M514 0 L730 0 L730 155 A160 160 0 0 1 514 0 Z" fill="#e8d6c8" role="img" aria-label="Foto: gepflegter Fuß auf Holzboden"/>
      <path d="M514 0 A160 160 0 0 0 730 155" fill="none" stroke="var(--green)" stroke-width="3"/>
      <path d="M0 444 Q365 380 730 445 L730 515 L0 515 Z" fill="var(--band)"/>
      <path d="M0 444 Q365 380 730 445" fill="none" stroke="var(--green)" stroke-width="2.5"/>
    </svg>

    <p class="brand">Sanft im Gang</p>

    <p class="services"><strong>Mein Leistungsportfolio:</strong> Medizinische Fußpflege · Therapie Diabetischer Fuß · Hilfe bei eingewachsenen Nägeln · Spangentherapie · Druckschutz / Orthose · Hilfe bei Hühneraugen, Schrunden · Unterstützung bei Nagel- und Fußpilzbehandlung · Fußmassage · Nagelprothetik</p>

    <div class="about">
      <h2>Über mich</h2>
      <p>Ich bin Lena Marwitz, gelernte<br>medizinische Fußpflegerin und Podo-<br>login in Ausbildung und möchte mich<br>ganz persönlich um die medizinische<br>Pflege und Verschönerung Ihres Fußes<br>kümmern. Mein Interesse im medizini-<br>schen Bereich sowie an verschiedenen<br>Behandlungsmethoden begleitet mich<br>schon mein ganzes Leben lang.</p>
    </div>

    <div class="prices">
      <h2>Preise</h2>
      <ul class="price-list">
        <li>Medizinische Fußpflege<span class="dots"></span>42,50 €</li>
        <li>Nagelkorrektur Ungilan<span class="dots"></span>40,00 €</li>
        <li>Teilbehandlung <span class="dots"></span>27,50 €</li>
        <li>Nagelprothetik<span class="dots"></span>31,80 €</li>
        <li>Tamponaden<span class="dots"></span>3,00 €</li>
        <li>Nagellack&nbsp;<small>(mit mitgebrachtem Lack)</small><span class="dots"></span>10,00 €</li>
      </ul>
    </div>

    <address class="address">Physio Praxis Brandauer<br>Lindenweg 4/2<br>71399 Horbenau</address>
    <p class="contact">Tel: +49 7100 555 21 40<br>Mobil: +49 1700 555 318<br>www.fusspflege-horbenau.de</p>
  </section>

</div>
</body>
</html>
```